RHS Trifold Brochure

Would like a Trifold Brochure to use for marketing purposes. The company, Reliable Home Solutions is a Handyman Service that offers Residential Home Repairs, Commercial Repairs, Drain Cleaning, Carpet Cleaning and Water Extraction.

I am attaching some pdf files to use as potential verbage and a copy of our business card and logo image file.

Would like to portray a professional image that sets us apart from a "mom and pops" type handyman service.

Industry/Entity Type

Marketing

```html
<!DOCTYPE html>
<html lang="en">
<head>
<meta charset="utf-8">
<title>RHS Trifold Brochure</title>
<link rel="stylesheet" href="https://fonts.googleapis.com/css2?family=Exo+2:ital,wght@0,300;0,400;0,700;0,800;1,300;1,400;1,700;1,800&family=Roboto+Condensed:wght@700&display=swap">
<style>
  :root {
    --navy: #15145f;
    --navy-deep: #0f0e4a;
    --indigo: #5a59a6;
    --lavender: #9c9bd4;
    --teal: #a9e3e6;
    --teal-soft: #d2f1f2;
    --paper: #eef0f2;
    --ink-white: #f4f4fb;
    --stage: #e4e5ea;
  }
  * { box-sizing: border-box; margin: 0; padding: 0; }
  html, body { width: 1200px; height: 1200px; overflow: hidden; }
  body {
    background: var(--stage);
    font-family: "Exo 2", sans-serif;
    position: relative;
  }
  .brochure {
    position: absolute;
    left: 40px; top: 166px;
    width: 1120px; height: 868px;
    background: var(--paper);
    overflow: hidden;
    box-shadow: 0 10px 30px rgba(20, 20, 60, 0.25);
  }
  .brochure__waves { position: absolute; inset: 0; width: 100%; height: 100%; }
  .abs { position: absolute; }

  .headline {
    left: 56px; top: 22px;
    color: var(--navy);
    font-weight: 800; font-style: italic;
    font-size: 34px; line-height: 1.1;
    transform: rotate(-2deg);
    transform-origin: left top;
  }

  .service {
    color: var(--ink-white);
    font-weight: 700; font-style: italic;
    font-size: 46px; line-height: 1;
    letter-spacing: 0.5px;
  }
  .service--plumbing { left: 30px; top: 312px; }
  .service--electrical { left: 110px; top: 402px; }
  .service--hvac { left: 268px; top: 484px; font-size: 40px; line-height: 0.95; }
  .service--condensed {
    font-family: "Roboto Condensed", sans-serif;
    font-style: normal; font-size: 40px; line-height: 0.98;
  }
  .service--interior { left: 432px; top: 596px; }
  .service--exterior { left: 506px; top: 706px; }

  .photo { border: 3px solid #fff; }
  .photo--tools {
    left: 56px; top: 572px; width: 272px; height: 198px;
    background: linear-gradient(135deg, #e9d3b3 0%, #c9a67a 45%, #f2f2f2 70%, #3f8fd0 100%);
  }
  .photo--home {
    left: 410px; top: 128px; width: 262px; height: 308px;
    border: none;
    background: radial-gradient(ellipse at 50% 45%, #e98a4c 0%, #e6c2a4 38%, #e9e4df 65%, rgba(238,240,242,0) 80%);
  }

  .call {
    left: 747px; width: 373px; text-align: center;
    color: var(--navy);
  }
  .call__label { top: 4px; font-weight: 800; font-style: italic; font-size: 42px; }
  .call__phone { top: 56px; font-weight: 300; font-size: 42px; letter-spacing: 0.5px; }

  .badge {
    left: 772px; top: 134px; width: 300px; height: 104px;
    background: var(--navy);
    border-radius: 14px;
    padding: 5px;
  }
  .badge__inner {
    width: 100%; height: 100%;
    border: 2px solid #fff;
    border-radius: 10px;
    display: flex; flex-direction: column; align-items: center; justify-content: center;
    color: #fff;
  }
  .badge__hours { font-weight: 700; font-size: 46px; line-height: 1; }
  .badge__note { font-weight: 400; font-size: 24px; line-height: 1.1; letter-spacing: -0.3px; }

  .brand {
    left: 747px; top: 322px; width: 373px; text-align: center;
    color: var(--navy);
    font-weight: 700; font-size: 40px; line-height: 1.05;
  }

  .why {
    right: 24px; top: 512px;
    color: var(--ink-white);
    font-weight: 800; font-style: italic; font-size: 54px;
  }
  .reasons {
    left: 768px; top: 604px; width: 340px;
    list-style: none;
    color: var(--ink-white);
    font-style: italic; font-weight: 400; font-size: 24px; line-height: 32px;
  }
  .reasons li { position: relative; padding-left: 34px; }
  .reasons svg { position: absolute; left: 0; top: 4px; width: 26px; height: 26px; }
</style>
</head>
<body>
  <section class="brochure" aria-label="Reliable Home Solutions trifold brochure">
    <svg class="brochure__waves" viewBox="0 0 1120 868" preserveAspectRatio="none" aria-hidden="true">
      <defs>
        <linearGradient id="lowerBand" x1="0" y1="0" x2="0" y2="1">
          <stop offset="0" stop-color="#6261ad"/>
          <stop offset="0.55" stop-color="#3b3a8a"/>
          <stop offset="1" stop-color="#15145f"/>
        </linearGradient>
        <linearGradient id="tealBand" x1="0" y1="0" x2="1" y2="0">
          <stop offset="0" stop-color="#9fdfe3"/>
          <stop offset="1" stop-color="#c8eef0"/>
        </linearGradient>
      </defs>
      <path d="M0,0 L760,0 C800,90 910,175 1120,185 L1120,262 C930,252 800,228 690,196 C500,138 300,138 0,168 Z" fill="url(#tealBand)"/>
      <path d="M0,192 C210,170 410,232 560,380 C700,500 860,556 1120,520 L1120,868 L0,868 Z" fill="var(--navy)"/>
      <path d="M560,380 C700,500 860,556 1120,520" fill="none" stroke="var(--lavender)" stroke-width="6"/>
      <path d="M0,470 C250,462 450,556 620,660 C790,762 960,706 1120,700 L1120,868 L0,868 Z" fill="url(#lowerBand)"/>
    </svg>

    <h1 class="abs headline">We are Available 24/7<br>for Emergency Water Extraction!!!</h1>

    <div class="abs service service--plumbing">Plumbing</div>
    <div class="abs service service--electrical">Electrical</div>
    <div class="abs service service--hvac">HVAC &amp;<br>Appliances</div>
    <div class="abs photo photo--tools" role="img" aria-label="Photo of painting and repair tools: brushes, roller and putty knife"></div>

    <div class="abs photo photo--home" role="img" aria-label="Photo of open hands holding a small model house"></div>
    <div class="abs service service--condensed service--interior">Interior<br>Services</div>
    <div class="abs service service--condensed service--exterior">Exterior<br>Services</div>

    <div class="abs call call__label">Call Today!!!</div>
    <div class="abs call call__phone">(555) 014 - 2276</div>

    <div class="abs badge">
      <div class="badge__inner">
        <span class="badge__hours">24 Hour</span>
        <span class="badge__note">Emergency Service</span>
      </div>
    </div>

    <div class="abs brand">Reliable Home<br>Solutions</div>

    <h2 class="abs why">Why Us?</h2>
    <ul class="abs reasons">
      <li><svg viewBox="0 0 26 26"><path d="M3 14 L10 21 L23 4" fill="none" stroke="#fff" stroke-width="3" stroke-linecap="round" stroke-linejoin="round"/></svg>Locally Owned &amp; Operated</li>
      <li><svg viewBox="0 0 26 26"><path d="M3 14 L10 21 L23 4" fill="none" stroke="#fff" stroke-width="3" stroke-linecap="round" stroke-linejoin="round"/></svg>Quality Drain Cleaning<br>Services</li>
      <li><svg viewBox="0 0 26 26"><path d="M3 14 L10 21 L23 4" fill="none" stroke="#fff" stroke-width="3" stroke-linecap="round" stroke-linejoin="round"/></svg>24 Hour Emergency Drain<br>Service</li>
      <li><svg viewBox="0 0 26 26"><path d="M3 14 L10 21 L23 4" fill="none" stroke="#fff" stroke-width="3" stroke-linecap="round" stroke-linejoin="round"/></svg>Affordable Pricing</li>
      <li><svg viewBox="0 0 26 26"><path d="M3 14 L10 21 L23 4" fill="none" stroke="#fff" stroke-width="3" stroke-linecap="round" stroke-linejoin="round"/></svg>Warranty Provided</li>
    </ul>
  </section>
</body>
</html>
```